依頼詳細
完成見学会にて使用する【のぼり旗】のデザインを募集いたします。
600x1800のサイズで【月々5万円台から(~でも可)】【ZEH】【注文住宅専門店】の3つを分かりやすく目に入りやすいデザインで作成をお願いします。
それぞれのキーワードの前後に言葉を付け加えても、無くても結構です。
(例)月々5万円台からの注文住宅!、月々5万円台からのマイホーム!
高性能 ZEH!、省エネ×創エネ ZEH!
手が届く注文住宅!など

色合いとフォントは弊社のロゴマークに合うようにお願いします。
文字の配置や大きさ等は、添付データに沿ったデザインではなくて結構です。
記載項目
キャッチフレーズ、注文住宅専門店、ロゴマーク、そよみねホーム記載の検索窓イメージ

サイズ→600x1800
希望イメージ
シンプル 複雑
単色 カラフル
暗い 明るい
日常 高級
遊び心 厳粛
未来的 伝統的
女性的 男性的
希望する色
黄・オレンジ系、緑系、茶系、添付ロゴに沿った色合い
納品ファイル
• 高解像度JPG (.jpg)
• イラストレーター形式 (.ai)
• フォトショップ形式 (.psd)
• PNG形式 (.png)
補足説明
のぼり旗で使用するロゴデータを追記しました。
よろしくお願いします。
■ 選んだ理由

掲載して欲しいキーワードが分かりやすかったため選びました。
配色も社内で評判が良く、文字も見やすかったです。

■ 提案者全員のお礼・コメント

沢山のステキなご提案をありがとうございました。
また機会がありましたら宜しくお願いいたします。

```html
<!DOCTYPE html>
<html lang="ja">
<head>
<meta charset="utf-8">
<title>ZEH住宅 のぼり旗 — そよみねホーム</title>
<link rel="stylesheet" href="https://fonts.googleapis.com/css2?family=M+PLUS+Rounded+1c:wght@700;800;900&display=swap">
<style>
  :root {
    --orange: #f39a1c;
    --orange-light: #f7b45a;
    --white: #ffffff;
    --brown: #8a5a2e;
    --grey-line: #9a9a9a;
    --grey-icon: #6e6e6e;
  }
  html, body {
    margin: 0;
    padding: 0;
    width: 1200px;
    height: 3596px;
    overflow: hidden;
    background: var(--white);
  }
  .banner {
    position: relative;
    width: 1200px;
    height: 3596px;
    background: var(--white);
    font-family: "M PLUS Rounded 1c", sans-serif;
    overflow: hidden;
  }
  .tagline {
    position: absolute;
    top: 86px;
    left: 0;
    width: 1200px;
    text-align: center;
    font-size: 78px;
    font-weight: 900;
    color: var(--orange);
    letter-spacing: 1px;
    white-space: nowrap;
    margin: 0;
    line-height: 1;
  }
  .panel {
    position: absolute;
    top: 0;
    left: 0;
    width: 1200px;
    height: 3596px;
  }
  .cycle-mark {
    position: absolute;
    left: 130px;
    top: 520px;
    width: 940px;
    height: 940px;
    border-radius: 50%;
    background: var(--orange-light);
    opacity: 0.55;
  }
  .headline {
    position: absolute;
    top: 0;
    left: 0;
    width: 1200px;
    height: 3000px;
  }
  .headline text {
    font-family: "M PLUS Rounded 1c", sans-serif;
    font-weight: 900;
  }
  .brand {
    position: absolute;
    left: 0;
    top: 3060px;
    width: 1200px;
    height: 300px;
  }
  .brand-square {
    position: absolute;
    left: 140px;
    top: 70px;
    width: 150px;
    height: 150px;
    background: var(--brown);
    border-radius: 10px;
  }
  .brand-sub {
    position: absolute;
    left: 520px;
    top: 60px;
    font-size: 44px;
    font-weight: 800;
    color: var(--brown);
    margin: 0;
    line-height: 1;
  }
  .brand-name {
    position: absolute;
    left: 330px;
    top: 120px;
    font-size: 112px;
    font-weight: 900;
    color: var(--brown);
    margin: 0;
    line-height: 1;
    letter-spacing: 2px;
    white-space: nowrap;
  }
  .search-box {
    position: absolute;
    left: 120px;
    top: 3360px;
    width: 960px;
    height: 100px;
    box-sizing: border-box;
    border: 4px solid var(--grey-line);
    border-radius: 50px;
    background: linear-gradient(#ffffff, #f1f1f1);
  }
  .search-text {
    position: absolute;
    left: 0;
    top: 0;
    width: 100%;
    line-height: 92px;
    text-align: center;
    font-size: 62px;
    font-weight: 700;
    color: #222;
    margin: 0;
    white-space: nowrap;
  }
  .search-icon {
    position: absolute;
    right: 40px;
    top: 16px;
    width: 64px;
    height: 64px;
  }
</style>
</head>
<body>
<main class="banner">
  <svg class="panel" viewBox="0 0 1200 3596" aria-hidden="true">
    <path d="M0 248 H1200 V2985 C1050 2940 900 2900 700 2930 C480 2965 260 2990 0 2905 Z" fill="var(--orange)"/>
  </svg>

  <p class="tagline">天然杉のぬくもりある暮らし</p>

  <div class="cycle-mark" role="img" aria-label="省エネと創エネの循環を表す矢印の装飾"></div>

  <svg class="headline" viewBox="0 0 1200 3000" aria-label="省エネ×創エネ ZEH住宅 月々5万円〜">
    <text x="600" y="660" text-anchor="middle" font-size="92" fill="var(--white)">省エネ×創エネ</text>

    <g text-anchor="middle" stroke-linejoin="round">
      <text x="605" y="1000" font-size="300" fill="none" stroke="var(--white)" stroke-width="36" letter-spacing="10">ZEH</text>
      <text x="605" y="1000" font-size="300" fill="var(--orange)" letter-spacing="10">ZEH</text>
      <text x="605" y="1000" font-size="300" fill="none" stroke="var(--white)" stroke-width="10" letter-spacing="10">ZEH</text>

      <text x="630" y="1360" font-size="320" fill="none" stroke="var(--white)" stroke-width="36" letter-spacing="60">住宅</text>
      <text x="630" y="1360" font-size="320" fill="var(--orange)" letter-spacing="60">住宅</text>
      <text x="630" y="1360" font-size="320" fill="none" stroke="var(--white)" stroke-width="10" letter-spacing="60">住宅</text>
    </g>

    <g>
      <ellipse cx="850" cy="1960" rx="210" ry="155" fill="var(--white)"/>
      <path d="M880 2090 L905 2175 L955 2075 Z" fill="var(--white)"/>
      <text x="850" y="2012" text-anchor="middle" font-size="150" fill="var(--orange)">月々</text>
    </g>

    <g stroke-linejoin="round">
      <text x="310" y="2800" text-anchor="middle" font-size="1040" fill="var(--white)" stroke="var(--white)" stroke-width="60">5</text>
      <text x="310" y="2800" text-anchor="middle" font-size="1040" fill="none" stroke="var(--orange)" stroke-width="12">5</text>
    </g>

    <path d="M650 2280 C710 2170 800 2170 870 2260 C930 2340 1010 2340 1080 2230"
          fill="none" stroke="var(--white)" stroke-width="60" stroke-linecap="round"/>
    <path d="M650 2280 C710 2170 800 2170 870 2260 C930 2340 1010 2340 1080 2230"
          fill="none" stroke="var(--orange)" stroke-width="12" stroke-linecap="round"/>

    <g text-anchor="middle" stroke-linejoin="round">
      <text x="880" y="2730" font-size="280" fill="var(--white)" stroke="var(--white)" stroke-width="24">万円</text>
      <text x="880" y="2730" font-size="280" fill="none" stroke="var(--orange)" stroke-width="8">万円</text>
    </g>
  </svg>

  <section class="brand">
    <div class="brand-square"></div>
    <p class="brand-sub">注文住宅専門店</p>
    <p class="brand-name">そよみねホーム</p>
  </section>

  <div class="search-box">
    <p class="search-text">そよみねホーム</p>
    <svg class="search-icon" viewBox="0 0 64 64" aria-hidden="true">
      <circle cx="26" cy="26" r="17" fill="none" stroke="var(--grey-icon)" stroke-width="7"/>
      <line x1="39" y1="39" x2="57" y2="57" stroke="var(--grey-icon)" stroke-width="9" stroke-linecap="round"/>
    </svg>
  </div>
</main>
</body>
</html>
```